Your 'not so average' farmers. We are farmers and entrepreneurs trying to connect the great divide.

HBQ (Thornwick Provision Inc) is a family owned farm (in our 3rd generation). We grow vegetables (corn, soy, potatoes, snap beans) but we also invest in and grow businesses. These other businesses can be non-farming related businesses. We are family oriented, environmentally concise, and active in our small community. We need a business card to hand out to our fellow farmers, businesses we would like to partner with and invest in, and community members. So, we need a card with a natural, 'tenders of the land' feel for the farmers but no overly so that we seem centered on farming for the other businesses. We would like it to have our Company info (name, number, email, phone, fax) then Personal info for us five who run the joint (Name, phone, email). So we will order 100 cards for each 5 who work at HBQ (500total) that is professional, not boring or hokey, but catching and unique.
Target Market(s)
Farmers, Business Owners, Investors, Community Members
Industry/Entity Type
Farming
Contact Information for Business Card
Office info on one side:
Thornwick Provision Inc.
1187 Cedar Row
Pell Hollow, WI 54872
Office: (608) 555-0147
Fax: (608) 555-0183
thornwickoffice@fieldpostmail.example
Personal Info for the 5 who run HBQ. Everybody will have their own personal info on their cards(maybe on the other side):
Name
Mobile
Email
Look and feel

```html
<!DOCTYPE html>
<html lang="en">
<head>
<meta charset="utf-8">
<title>Thornwick Provision Inc – Business Card</title>
<link rel="stylesheet" href="https://fonts.googleapis.com/css2?family=Arimo:wght@400;700&display=swap">
<style>
  :root{
    --bg:#eceae6;
    --green:#17813c;
    --green-dark:#0f6b31;
    --green-light:#24994a;
    --orange:#e2631d;
    --ink:#1d1d1d;
    --soft-white:#f2f2f2;
    --faint:#e6e6e6;
    --paper:#ffffff;
  }
  *{box-sizing:border-box;margin:0;padding:0}
  html,body{width:1200px;height:784px;overflow:hidden}
  body{background:var(--bg);font-family:"Arimo",Arial,sans-serif;position:relative}

  .card{position:absolute;width:530px;height:303px;overflow:hidden;
        box-shadow:0 4px 14px rgba(0,0,0,.18)}

  /* Back side */
  .card--back{left:40px;top:240px;
    background:linear-gradient(180deg,var(--green-light) 0%,var(--green) 55%,var(--green-dark) 100%);}
  .card--back .mark{position:absolute;left:0;right:0;top:78px;display:flex;
    justify-content:center;align-items:center;gap:14px}
  .card--back .mark-name{font-weight:700;font-size:92px;color:var(--orange);letter-spacing:2px;line-height:1}
  .card--back .mark-dot{width:22px;height:22px;border-radius:50%;background:var(--soft-white)}
  .card--back .company{position:absolute;left:0;right:0;top:206px;text-align:center;
    color:var(--soft-white);font-size:19px;letter-spacing:9px}

  /* Front side */
  .card--front{left:630px;top:240px;background:var(--paper)}
  .card--front .watermark{position:absolute;right:-18px;top:70px;font-weight:700;
    font-size:118px;color:var(--faint);line-height:1}
  .person{position:absolute;right:22px;top:18px;text-align:right;line-height:1.35}
  .person-name{color:var(--orange);font-size:15px}
  .person-line{color:var(--ink);font-size:11px}

  .brand{position:absolute;left:30px;top:62px}
  .brand-mark{display:flex;align-items:center;gap:8px}
  .brand-name{font-weight:700;font-size:58px;color:var(--orange);line-height:1;letter-spacing:1px}
  .brand-dot{width:14px;height:14px;border-radius:50%;background:var(--green)}
  .brand-company{margin-top:4px;font-weight:700;font-size:15px;color:var(--ink)}

  .contact{position:absolute;left:30px;top:170px;list-style:none;font-size:14.5px;color:var(--ink)}
  .contact li{display:flex;align-items:flex-start;gap:7px;line-height:1.2;margin-bottom:2px}
  .contact svg{width:14px;height:14px;flex:none;margin-top:2px;fill:var(--orange)}

  .rule{position:absolute;left:0;right:0;bottom:34px;height:3px;background:var(--orange)}
  .band{position:absolute;left:0;right:0;bottom:0;height:31px;
    background:linear-gradient(180deg,var(--green-light),var(--green-dark))}
</style>
</head>
<body>

<section class="card card--back" aria-label="Card back">
  <div class="mark">
    <span class="mark-name">HBQ</span>
    <span class="mark-dot"></span>
  </div>
  <p class="company">Thornwick Provision Inc</p>
</section>

<section class="card card--front" aria-label="Card front">
  <span class="watermark" aria-hidden="true">HBQ</span>

  <div class="person">
    <p class="person-name">Mara Lindqvist</p>
    <p class="person-line">1685 555 012</p>
    <p class="person-line">maralind@fieldpostmail.example</p>
  </div>

  <div class="brand">
    <div class="brand-mark">
      <span class="brand-name">HBQ</span>
      <span class="brand-dot"></span>
    </div>
    <p class="brand-company">Thornwick Provision Inc</p>
  </div>

  <ul class="contact">
    <li>
      <svg viewBox="0 0 24 24" aria-hidden="true"><path d="M6.6 10.8a15.1 15.1 0 0 0 6.6 6.6l2.2-2.2c.3-.3.7-.4 1-.2 1.1.4 2.3.6 3.6.6.6 0 1 .4 1 1V20c0 .6-.4 1-1 1A17 17 0 0 1 3 4c0-.6.4-1 1-1h3.5c.6 0 1 .4 1 1 0 1.3.2 2.5.6 3.6.1.3 0 .7-.2 1z"/></svg>
      <span>(608) 555-0147</span>
    </li>
    <li>
      <svg viewBox="0 0 24 24" aria-hidden="true"><path d="M7 3h10v5H7zM4 9h16a2 2 0 0 1 2 2v6h-4v4H6v-4H2v-6a2 2 0 0 1 2-2zm4 7v3h8v-3z"/></svg>
      <span>(608) 555-0183</span>
    </li>
    <li>
      <svg viewBox="0 0 24 24" aria-hidden="true"><path d="M3 5h18v14H3zm2 2v.5l7 5 7-5V7l-7 5z"/></svg>
      <span>thornwickoffice@fieldpostmail.example</span>
    </li>
    <li>
      <svg viewBox="0 0 24 24" aria-hidden="true"><path d="M12 3l10 9h-3v9h-5v-6h-4v6H5v-9H2z"/></svg>
      <span>1187 Cedar Row, Pell Hollow,<br>WI 54872</span>
    </li>
  </ul>

  <div class="rule"></div>
  <div class="band"></div>
</section>

</body>
</html>
```